Biz Cards for Lumivale Associates

Lumivale Associates is seeking a single-sided business card that is more visually-appealing than our current design (see attached).

Notes:
- Our colors are blue & teal.
- Our tag line must be large enough to be easily read
- We don't necessarily need our address included (that's just the biz office)
- We'd like to add our email address: Lumivale512@brindlemail.net

Thanks!

Industry/Entity Type

Business

Contact Information for Business Card

Standard size
PSD file required w/ text on its own layer

Colors
86cfc6
3277b5

```html
<!DOCTYPE html>
<html lang="en">
<head>
<meta charset="utf-8">
<title>Lumivale Associates – Business Card</title>
<link rel="stylesheet" href="https://fonts.googleapis.com/css2?family=Arimo:wght@400&family=Open+Sans:ital,wght@0,400;0,600;1,400&display=swap">
<style>
  :root {
    --bg: #e9eaec;
    --card: #fbfbfa;
    --ink: #1d1d1f;
    --blue: #3277b5;
    --blue-bright: #2f8fd6;
    --teal: #86cfc6;
    --logo-ink: #2a2a2c;
  }
  * { margin: 0; padding: 0; box-sizing: border-box; }
  html, body {
    width: 1200px; height: 799px; overflow: hidden;
    background: var(--bg);
  }
  .card {
    position: absolute; left: 100px; top: 114px;
    width: 1000px; height: 571px;
    background: var(--card);
    box-shadow: 0 10px 30px rgba(0,0,0,.12);
    font-family: "Open Sans", sans-serif;
    color: var(--ink);
  }
  .accent-bar {
    position: absolute; left: 44px; top: 50px;
    width: 16px; height: 64px;
    background: linear-gradient(180deg, var(--blue-bright), var(--teal));
  }
  .holder-name {
    position: absolute; left: 76px; top: 44px;
    font-family: "Arimo", sans-serif; font-size: 42px; letter-spacing: .5px;
    white-space: nowrap;
  }
  .holder-title {
    position: absolute; left: 78px; top: 96px;
    font-family: "Arimo", sans-serif; font-size: 25px; color: var(--blue-bright);
    white-space: nowrap;
  }
  .contacts {
    position: absolute; left: 44px; top: 212px; list-style: none;
  }
  .contacts li {
    display: flex; align-items: center; gap: 14px;
    font-size: 23px; line-height: 40px; white-space: nowrap;
  }
  .contacts svg { width: 24px; height: 24px; flex: none; }
  .divider {
    position: absolute; left: 0; top: 388px;
    width: 720px; height: 3px; background: var(--blue-bright);
  }
  .website {
    position: absolute; left: 24px; top: 400px;
    font-size: 22px; color: var(--blue);
  }
  .brand {
    position: absolute; left: 560px; top: 230px; width: 410px;
    display: flex; align-items: center; gap: 16px;
  }
  .brand-dot {
    width: 70px; height: 70px; border-radius: 50%;
    background: var(--teal); flex: none;
  }
  .brand-name {
    font-family: "Open Sans", sans-serif; font-weight: 600;
    font-size: 34px; line-height: 1.1; color: var(--logo-ink);
  }
  .tagline {
    position: absolute; left: 560px; top: 330px;
    font-size: 20px; font-style: italic; color: var(--blue);
    white-space: nowrap;
  }
  .social {
    position: absolute; left: 760px; top: 470px;
    display: flex; gap: 22px;
  }
  .social span {
    width: 30px; height: 30px; border-radius: 4px;
    background: var(--blue-bright); display: block;
  }
</style>
</head>
<body>
  <div class="card">
    <div class="accent-bar"></div>
    <div class="holder-name">Dana Whitfield, RN</div>
    <div class="holder-title">Mental Health Therapist</div>

    <ul class="contacts">
      <li>
        <svg viewBox="0 0 24 24" aria-hidden="true"><path fill="#3277b5" d="M3 8c0-2 3-4 9-4s9 2 9 4v2h-5V8H8v2H3zM6 11h12l2 8H4z"/><circle cx="12" cy="15" r="2.5" fill="#fbfbfa"/></svg>
        <span>(855) LUMI-VAL</span>
      </li>
      <li>
        <svg viewBox="0 0 24 24" aria-hidden="true"><rect x="7" y="3" width="10" height="7" fill="#3277b5"/><rect x="3" y="10" width="18" height="9" rx="2" fill="#3277b5"/><rect x="7" y="15" width="10" height="6" fill="#86cfc6"/></svg>
        <span>(330) 555-0184</span>
      </li>
      <li>
        <svg viewBox="0 0 24 24" aria-hidden="true"><rect x="2" y="5" width="20" height="14" fill="#3277b5"/><path d="M2 5l10 8 10-8" fill="none" stroke="#fbfbfa" stroke-width="1.5"/></svg>
        <span>Lumivale512@brindlemail.net</span>
      </li>
    </ul>

    <div class="divider"></div>
    <div class="website">Lumivale.net</div>

    <div class="brand">
      <div class="brand-dot"></div>
      <div class="brand-name">Lumivale Associates Ltd</div>
    </div>
    <div class="tagline">Clear Thinking. Kind Hearts. Steady Care.</div>

    <div class="social" aria-label="Social media">
      <span></span><span></span><span></span>
    </div>
  </div>
</body>
</html>
```